Dental Consulting Business Card - Stationary
Business Card / Stationary
Modern
Glen R. Castellano
President
4817 W. Harborview Ave.
Fort Lauderdale, FL
glen@zuvadentalconsulting.example
www.zuvadentalconsulting.example

```html
<!DOCTYPE html>
<html lang="en">
<head>
<meta charset="utf-8">
<title>ZuvaDental Stationery</title>
<link href="https://fonts.googleapis.com/css2?family=Nunito:wght@400;700;800&display=swap" rel="stylesheet">
<style>
  :root {
    --blue: #1f86c8;
    --charcoal: #3d3f42;
    --paper: #ffffff;
    --backdrop: #d7d8da;
    --ink: #4a4c50;
    --light: #e9f3fa;
  }
  * { box-sizing: border-box; margin: 0; padding: 0; }
  html, body { width: 1200px; height: 683px; overflow: hidden; }
  body {
    position: relative;
    background: var(--backdrop);
    font-family: "Nunito", sans-serif;
    color: var(--ink);
  }
  .piece {
    position: absolute;
    background: var(--paper);
    box-shadow: 0 3px 10px rgba(0,0,0,.18);
    overflow: hidden;
  }
  .brand {
    font-weight: 800;
    color: var(--charcoal);
    display: flex;
    align-items: center;
    gap: 6px;
    white-space: nowrap;
  }
  .brand-dot { width: 10px; height: 10px; background: var(--blue); flex: none; }

  /* Letterheads */
  .letterhead { top: 30px; width: 320px; height: 414px; }
  .letterhead.first { left: 440px; }
  .letterhead.second { left: 790px; }
  .letterhead .top-rule { height: 6px; background: var(--charcoal); }
  .letterhead .band {
    position: relative;
    margin-top: 4px;
    height: 30px;
    background: var(--blue);
  }
  .letterhead .logo-block {
    position: absolute; left: 10px; top: -8px;
    height: 44px; padding: 0 10px;
    background: var(--paper);
    border-radius: 0 0 6px 6px;
    display: flex; align-items: center;
  }
  .letterhead .brand { font-size: 17px; }
  .letterhead .contact {
    position: absolute; right: 10px; top: 3px;
    text-align: right; color: var(--paper);
    font-size: 5.5px; line-height: 1.35;
  }

  /* Envelopes */
  .envelope { left: 30px; width: 370px; height: 175px; }
  .envelope.back { top: 30px; }
  .envelope.front-a { top: 235px; }
  .envelope.front-b { top: 440px; }
  .envelope.back .flap {
    position: absolute; left: 0; top: 0; width: 100%; height: 70px;
    background: var(--charcoal);
  }
  .envelope.back .flap-stripe {
    position: absolute; left: 0; top: 70px; width: 100%; height: 8px;
    background: var(--blue);
  }
  .envelope.back .brand {
    position: absolute; left: 128px; top: 22px;
    font-size: 22px; color: var(--paper);
  }
  .envelope .top-rule { position: absolute; left: 0; top: 18px; width: 100%; height: 6px; background: var(--charcoal); }
  .envelope .band { position: absolute; left: 0; top: 28px; width: 100%; height: 26px; background: var(--blue); }
  .envelope .logo-block {
    position: absolute; left: 12px; top: 12px;
    height: 46px; padding: 0 10px;
    background: var(--paper);
    border-radius: 6px;
    display: flex; align-items: center;
  }
  .envelope .brand { font-size: 18px; }
  .envelope .return-address {
    position: absolute; left: 22px; top: 66px;
    font-size: 6px; line-height: 1.4; color: var(--ink);
  }

  /* Business cards */
  .card {
    top: 470px; width: 330px; height: 189px;
    background: var(--charcoal);
    border-radius: 16px;
    color: var(--paper);
  }
  .card.front { left: 440px; }
  .card.back { left: 800px; }
  .card.front .brand {
    position: absolute; left: 34px; top: 36px;
    font-size: 34px; color: var(--paper);
  }
  .card.front .brand-dot { width: 16px; height: 16px; }
  .card.front .band {
    position: absolute; left: 0; top: 104px; width: 100%; height: 34px;
    background: var(--blue);
  }
  .card.front .tagline {
    position: absolute; left: 0; top: 146px; width: 100%;
    text-align: center; font-size: 12px; font-weight: 700; letter-spacing: .4px;
  }
  .card.back .band {
    position: absolute; left: 0; top: 46px; width: 100%; height: 44px;
    background: var(--blue);
    padding: 6px 22px;
  }
  .card.back .name { font-size: 16px; font-weight: 800; line-height: 1.1; }
  .card.back .title { font-size: 10px; font-weight: 700; }
  .card.back .details {
    position: absolute; left: 22px; top: 104px;
    font-size: 9px; line-height: 1.5;
  }
  .card.back .brand {
    position: absolute; left: 22px; top: 16px;
    font-size: 14px; color: var(--paper);
  }
</style>
</head>
<body>

  <section class="piece envelope back">
    <div class="flap"></div>
    <div class="flap-stripe"></div>
    <div class="brand"><span class="brand-dot"></span>ZuvaDental</div>
  </section>

  <section class="piece envelope front-a">
    <div class="top-rule"></div>
    <div class="band"></div>
    <div class="logo-block"><div class="brand"><span class="brand-dot"></span>ZuvaDental</div></div>
    <address class="return-address">4817 W. Harborview Ave.<br>Fort Lauderdale, FL</address>
  </section>

  <section class="piece envelope front-b">
    <div class="top-rule"></div>
    <div class="band"></div>
    <div class="logo-block"><div class="brand"><span class="brand-dot"></span>ZuvaDental</div></div>
    <address class="return-address">4817 W. Harborview Ave.<br>Fort Lauderdale, FL</address>
  </section>

  <section class="piece letterhead first">
    <div class="top-rule"></div>
    <div class="band">
      <div class="logo-block"><div class="brand"><span class="brand-dot"></span>ZuvaDental</div></div>
      <address class="contact">4817 W. Harborview Ave., Fort Lauderdale, FL<br>glen@zuvadentalconsulting.example<br>www.zuvadentalconsulting.example</address>
    </div>
  </section>

  <section class="piece letterhead second">
    <div class="top-rule"></div>
    <div class="band">
      <div class="logo-block"><div class="brand"><span class="brand-dot"></span>ZuvaDental</div></div>
      <address class="contact">4817 W. Harborview Ave., Fort Lauderdale, FL<br>glen@zuvadentalconsulting.example<br>www.zuvadentalconsulting.example</address>
    </div>
  </section>

  <section class="piece card front">
    <div class="brand"><span class="brand-dot"></span>ZuvaDental</div>
    <div class="band"></div>
    <p class="tagline">Marketing - Media - Management</p>
  </section>

  <section class="piece card back">
    <div class="brand"><span class="brand-dot"></span>ZuvaDental</div>
    <div class="band">
      <p class="name">Glen R. Castellano</p>
      <p class="title">President</p>
    </div>
    <address class="details">4817 W. Harborview Ave.<br>Fort Lauderdale, FL<br>glen@zuvadentalconsulting.example<br>www.zuvadentalconsulting.example</address>
  </section>

</body>
</html>
```